Meridian Rest Supply Needs Business Card

Looking for a very nice looking business card. Creative but not extravagant. We sell beds and pillows across the U.S. and need something professional but catchy. I have attached the logo.

Name : Dale Fenwick
Title : President
Phone : (800) 417-2964
Email: sleep@quorvana.com
Website: www.quorvana.com

Can be single-sided or double-sided
horizontal or vertical

Can use Blues/Greys

Target Market(s)

Mass Market

Industry/Entity Type

Retail

Contact Information for Business Card

Name : Dale Fenwick
Title : President
Phone : (800) 417-2964
Email: sleep@quorvana.com
Website: www.quorvana.com

Requirements
Must have
• Clean, Modern, Smooth
• Can use Blues/Greys
• On the other side without the information - have something simple like www.quorvana.com or our logo
Nice to have
• Surprise me
Should not have
• Nothing crazy, nothing cluttered

```html
<!DOCTYPE html>
<html lang="en">
<head>
<meta charset="utf-8">
<title>Quorvana Business Card</title>
<link rel="stylesheet" href="https://fonts.googleapis.com/css2?family=Quicksand:wght@400;500;600&display=swap">
<style>
  :root {
    --canvas-bg: #e9edf1;
    --card-white: #ffffff;
    --brand-blue: #2a9bd8;
    --brand-blue-deep: #1f88c4;
    --brand-blue-light: #5cb8e8;
    --ink-grey: #3f3f42;
    --band-grey: #5e5e60;
    --back-text: #e8f3fa;
  }
  * { box-sizing: border-box; margin: 0; padding: 0; }
  html, body {
    width: 1200px; height: 900px; overflow: hidden;
    background: var(--canvas-bg);
    font-family: "Quicksand", sans-serif;
  }
  .sheet {
    width: 1200px; height: 900px;
    display: flex; flex-direction: column; align-items: center; justify-content: center;
    gap: 48px;
  }
  .card {
    position: relative;
    width: 660px; height: 377px;
    overflow: hidden;
    box-shadow: 0 6px 18px rgba(30, 50, 70, 0.18);
  }
  .card-front { background: var(--card-white); }
  .card-back { background: var(--brand-blue-deep); }

  .front-decoration { position: absolute; inset: 0; width: 100%; height: 100%; }

  .wordmark {
    position: absolute;
    font-weight: 400;
    letter-spacing: 1px;
    line-height: 1;
  }
  .card-front .wordmark {
    left: 48px; top: 150px;
    font-size: 58px;
    color: var(--brand-blue);
  }
  .contact {
    position: absolute;
    left: 372px; top: 92px;
  }
  .contact-name {
    font-size: 25px; font-weight: 500; color: var(--ink-grey);
    line-height: 1.1;
  }
  .contact-title {
    font-size: 16px; font-weight: 500; color: var(--brand-blue);
    margin: 2px 0 10px 10px;
  }
  .contact-list { list-style: none; margin-left: 18px; }
  .contact-list li {
    display: flex; align-items: center; gap: 8px;
    font-size: 15px; font-weight: 500; color: var(--ink-grey);
    line-height: 1.65;
  }
  .contact-list svg { width: 13px; height: 13px; flex: none; fill: var(--brand-blue); }

  .card-back .wordmark {
    left: 0; right: 0; top: 130px; text-align: center;
    font-size: 72px;
    color: var(--back-text);
  }
  .back-url {
    position: absolute; left: 0; right: 0; top: 250px; text-align: center;
    font-size: 14px; font-weight: 500; letter-spacing: 0.5px;
    color: var(--back-text);
  }
</style>
</head>
<body>
<main class="sheet">
  <section class="card card-front">
    <svg class="front-decoration" viewBox="0 0 660 377" aria-hidden="true">
      <rect x="300" y="288" width="360" height="8" fill="var(--band-grey)"/>
      <polygon points="78,296 155,296 138,377 58,377" fill="var(--band-grey)"/>
      <polygon points="155,296 262,296 252,377 138,377" fill="var(--brand-blue)"/>
      <polygon points="262,296 308,296 300,352 252,377" fill="var(--brand-blue-light)"/>
      <rect x="0" y="346" width="70" height="7" fill="var(--band-grey)"/>
    </svg>
    <div class="wordmark">quorvana</div>
    <div class="contact">
      <p class="contact-name">Dale Fenwick</p>
      <p class="contact-title">President</p>
      <ul class="contact-list">
        <li>
          <svg viewBox="0 0 16 16"><path d="M2 5c0-2 2-3 6-3s6 1 6 3v1h-3V5H5v1H2zM4 7h8l2 6H2zm4 1.5a2 2 0 100 4 2 2 0 000-4z"/></svg>
          (800) 417-2964
        </li>
        <li>
          <svg viewBox="0 0 16 16"><path d="M1 3h14v10H1zm1.5 1.5L8 9l5.5-4.5z"/></svg>
          sleep@quorvana.com
        </li>
        <li>
          <svg viewBox="0 0 16 16"><path d="M8 1a7 7 0 100 14A7 7 0 008 1zm0 1.5c1 1 1.6 2.6 1.7 4.7H6.3C6.4 5.1 7 3.5 8 2.5zM2.6 7.2A5.5 5.5 0 015.4 3c-.5 1.1-.9 2.6-1 4.2zm0 1.6h1.8c.1 1.6.5 3.1 1 4.2a5.5 5.5 0 01-2.8-4.2zM8 13.5c-1-1-1.6-2.6-1.7-4.7h3.4c-.1 2.1-.7 3.7-1.7 4.7zm2.6-.5c.5-1.1.9-2.6 1-4.2h1.8a5.5 5.5 0 01-2.8 4.2zm1-5.8c-.1-1.6-.5-3.1-1-4.2a5.5 5.5 0 012.8 4.2z"/></svg>
          www.quorvana.com
        </li>
      </ul>
    </div>
  </section>

  <section class="card card-back">
    <div class="wordmark">quorvana</div>
    <p class="back-url">www.quorvana.com</p>
  </section>
</main>
</body>
</html>
```